New Business Card for Innovative Tool Company

We need a new design of business card for our florida based tool manufacturing company. I will attach 2 files that we use for our logo, use whichever you feel works best for the card. Main colours are as per logo, and we can use different shades of black/white/grey for the background.

Contact Information for Business Card

Name/Jobtitle/cell
Corvalen Tools
Suite 212c
4316 Marrowdale Pkw
Orlando, FL32847
USA
name@corvaleninc.example
www.corvaleninc.example

Font styles to use
Sans Serif

Colors

Designer to choose colors to be used in the design.

Requirements
Must have
• Icons for Plazaro, Chirpet, Snapvale, Findlo & Vidstream

```html
<!DOCTYPE html>
<html lang="en">
<head>
<meta charset="utf-8">
<title>Corvalen Tools – Business Card</title>
<link href="https://fonts.googleapis.com/css2?family=Open+Sans:wght@400;600;700&display=swap" rel="stylesheet">
<style>
  :root {
    --backdrop: #2b2b2d;
    --card: #1c1c1e;
    --card-back: #202022;
    --accent: #f1e40f;
    --text: #e6e6e6;
    --muted: #bdbdbd;
    --rule: #3a3a3c;
    --pattern-top: #262628;
    --pattern-bottom: #1f1f21;
    --logo-light: #d9d9d9;
  }
  * { box-sizing: border-box; margin: 0; padding: 0; }
  html, body {
    width: 1200px; height: 1108px; overflow: hidden;
    background: var(--backdrop);
    font-family: "Open Sans", sans-serif;
  }
  .stage {
    width: 1200px; height: 1108px;
    display: flex; align-items: center; justify-content: center; gap: 80px;
  }
  .card {
    width: 400px; height: 640px; border-radius: 22px;
    box-shadow: 0 18px 40px rgba(0,0,0,.45);
    position: relative; overflow: hidden;
  }
  .card--front {
    background: var(--card);
    display: flex; flex-direction: column; align-items: center;
    padding-top: 150px; text-align: center;
  }
  .brand {
    display: flex; flex-direction: column; align-items: center; gap: 10px;
  }
  .brand__mark {
    width: 58px; height: 58px; border-radius: 50%;
    border: 2px solid currentColor;
  }
  .brand__name {
    font-weight: 700; font-size: 36px; letter-spacing: 2px;
    text-transform: uppercase; line-height: 1;
  }
  .card--front .brand { color: var(--accent); }
  .person { margin-top: 78px; }
  .person__name {
    color: var(--accent); font-weight: 700; font-size: 22px;
    text-transform: uppercase; letter-spacing: .3px;
  }
  .person__title { color: var(--muted); font-size: 16px; margin-top: 2px; }
  .rule { width: 210px; height: 1px; background: var(--rule); margin: 12px 0; }
  .address { color: var(--text); font-size: 16px; line-height: 1.35; }
  .address__company { color: var(--accent); text-transform: uppercase; font-size: 16px; }
  .contact { color: var(--text); font-size: 16px; line-height: 1.45; }
  .contact__label { color: var(--accent); font-weight: 700; }
  .contact__web { color: var(--accent); }

  .card--back { background: var(--card-back); }
  .pattern {
    position: absolute; inset: 0 0 220px 0;
    background: linear-gradient(180deg, var(--pattern-top), var(--pattern-bottom));
  }
  .back-brand {
    position: absolute; left: 0; right: 0; bottom: 96px;
    color: var(--logo-light);
  }
  .social {
    position: absolute; left: 0; right: 0; bottom: 40px;
    display: flex; justify-content: center; gap: 12px;
    color: var(--muted); font-size: 11px;
  }
  .social__item { display: flex; align-items: center; gap: 4px; }
  .social__dot { width: 10px; height: 10px; border-radius: 50%; background: var(--muted); }
</style>
</head>
<body>
<main class="stage">
  <section class="card card--front">
    <div class="brand">
      <span class="brand__mark"></span>
      <span class="brand__name">Corvalen Tools</span>
    </div>
    <div class="person">
      <p class="person__name">Dorian Kessler</p>
      <p class="person__title">Managing Director</p>
    </div>
    <div class="rule"></div>
    <div class="address">
      <p class="address__company">Corvalen Tools</p>
      <p>Suite 212c 4316 Marrowdale</p>
      <p>Pkw Orlando, FL32847 USA</p>
    </div>
    <div class="rule"></div>
    <div class="contact">
      <p><span class="contact__label">M:</span> 858 4471 2036</p>
      <p><span class="contact__label">E:</span> name@corvaleninc.example</p>
      <p class="contact__web">www.corvaleninc.example</p>
    </div>
  </section>

  <section class="card card--back">
    <div class="pattern" role="img" aria-label="Faint repeating brand symbol pattern"></div>
    <div class="brand back-brand">
      <span class="brand__mark"></span>
      <span class="brand__name">Corvalen Tools</span>
    </div>
    <ul class="social">
      <li class="social__item"><span class="social__dot"></span>Plazaro</li>
      <li class="social__item"><span class="social__dot"></span>Findlo</li>
      <li class="social__item"><span class="social__dot"></span>Vidstream</li>
      <li class="social__item"><span class="social__dot"></span>Chirpet</li>
      <li class="social__item"><span class="social__dot"></span>Snapvale</li>
    </ul>
  </section>
</main>
</body>
</html>
```